Morvena Designs - Online Shoe Shop

Morvena is an online shoes and bags shop. We sell Imported Genuine Leather shoes and bags our market is LSM 8-10. We mainly sell women shoes and bags and we will also be introducing men’s shoes and belts.
I would like a website design and development that is responsive, clean, elegant and easy to use. Where customers can make a purchase online.
Have CATEGORIES in SHOE STYLE (i.e. Heels, Sandals, Pumps, Mules, Boots, Sneaker, Flats, etc) and PRICE RANGE should be in South African Rands currency, COLOUR, SIZE.
For shoe images we should be able to add videos as well.
Header and Footer Menu should have the basic menu list. Header Menu (New Arrivals, Preorder, Women’s Collection, Men’s Collection, Summer 2020 Collection, Winter 2020 Collection, Bags, Accessories, Sale, etc
Auto display when the item is SOLD OUT. Add an option for a user to get notification on when the item is back in stock.
Icons to show when shoes are on sale and Show was and now price.
Users to be able to review and rate the items.
Discount codes for new email subscribers.
Consumers should be able to pay using different options, Credit card, CoinLane, EFT, etc
Add an option for discount coupons at checkout.
After placing and order they should receive an email with order receipt.
Site should have a shipping and tracking option. International shipping such as QRT and SWIFTBOX. For local shipping in South Africa please add Redtrail Couriers and Ulvoro Couriers.
Backend: Backend should be easy to add more categories, items and changing header banners, adding sale alerts. To get notification when the stock is low and sold out. Get notification when an order is placed online so to prepare packing for shipping.
Can we make sure that the SEO is in place and bare in mind all searchly rules to avoid being penalized.
Target Market(s)
Women from age 25-65
LSM 8-10
Entire South Africa and neighboring countries
Industry/Entity Type
Shoe Store
Coding
Coded - Design and coding required
Number of Pages Required
5+ page
Requirements
Must have
- Responsive
Clean
Modern
Shopping cart
Shipping options integration
Newsletter subscription
Social media icons
Nice to have
- The business colors are Gold and White or Gold and Black

```html
<!DOCTYPE html>
<html lang="en">
<head>
<meta charset="utf-8">
<title>Morvena – Shoes &amp; Bags</title>
<link href="https://fonts.googleapis.com/css2?family=Roboto:wght@300;400;500;700;900&display=swap" rel="stylesheet">
<style>
:root{
  --gold:#e8a200;
  --orange:#f2a20d;
  --red:#e2361a;
  --ink:#111;
  --text:#333;
  --muted:#666;
  --line:#cfcfcf;
  --dark:#1c1c1c;
  --blush:#f8d9dc;
}
*{box-sizing:border-box;margin:0;padding:0}
html,body{width:1200px;height:3602px;overflow:hidden}
body{font-family:'Roboto',sans-serif;color:var(--text);background:#fff;position:relative}
.abs{position:absolute}
a{color:inherit;text-decoration:none}

/* top bar */
.topbar{top:0;left:0;width:1200px;height:35px;border-bottom:1px solid #e3e3e3;font-size:11px;color:#444}
.topbar .welcome{left:94px;top:11px}
.topbar .lang{right:94px;top:11px}

/* header */
.header{top:35px;left:0;width:1200px;height:60px}
.brand{left:94px;top:6px;display:flex;flex-direction:column;align-items:center}
.brand .mark{width:26px;height:26px;background:var(--ink)}
.brand .name{font-size:14px;font-weight:700;color:var(--ink);margin-top:2px}
.search{left:403px;top:19px;width:395px;height:26px;border:1px solid #bbb;display:flex;font-size:10px;color:#666}
.search .cat{width:102px;border-right:1px solid #bbb;padding:6px 10px}
.search .field{flex:1;padding:7px 8px}
.search .btn{width:30px;background:var(--ink);display:flex;align-items:center;justify-content:center}
.hicons{right:94px;top:18px;display:flex;align-items:center;gap:14px;font-size:12px;color:#444}
.hicons .ico{width:28px;height:26px;background:var(--ink);display:inline-flex;align-items:center;justify-content:center;margin-right:8px;vertical-align:middle}

/* nav */
.nav{top:95px;left:0;width:1200px;height:40px;background:var(--ink);color:#fff}
.nav .cats{left:94px;top:0;width:182px;height:40px;background:#3a3a3a;display:flex;align-items:center;padding:0 14px;font-size:14px;font-weight:500;gap:10px}
.nav .cats .chev{margin-left:auto;width:18px;height:18px;border-radius:50%;background:#fff;display:flex;align-items:center;justify-content:center}
.nav ul{list-style:none;left:335px;top:0;height:40px;display:flex;align-items:center;gap:21px;font-size:12px}

/* hero */
.hero{top:135px;left:0;width:1200px;height:465px;background:#f6eee6}
.hero .model{left:108px;top:15px;width:330px;height:450px;background:linear-gradient(180deg,#d9cfc6,#8f8a86);border-radius:4px}
.hero .boots{left:812px;top:10px;width:300px;height:420px;background:linear-gradient(160deg,#5a5a5a,#1e1e1e 60%,#c22 95%);border-radius:6px}
.hero .hero-copy{left:420px;top:155px;width:410px;text-align:center}
.hero .kicker{color:var(--gold);letter-spacing:6px;font-size:14px}
.hero h1{font-size:50px;line-height:54px;font-weight:500;color:#222;margin-top:8px}
.hero .tag{display:inline-block;margin-top:14px;background:var(--gold);color:#fff;font-size:14px;font-weight:500;padding:8px 44px}
.dots{left:604px;top:421px;display:flex;gap:6px}
.dots i{width:9px;height:9px;border-radius:50%;background:#ccc}
.dots i:first-child{background:#111}

/* promos */
.promo{top:674px;height:163px}
.promo1{left:94px;width:327px;background:var(--blush)}
.promo1 .pic{left:14px;top:8px;width:150px;height:145px;background:linear-gradient(135deg,#d8c6ec,#b89ad8);border-radius:8px}
.promo1 .txt{left:178px;top:46px;font-size:17px;color:#222}
.promo1 .off{color:var(--red);font-size:22px;margin-top:2px}
.promo1 .shop{font-size:11px;font-weight:700;text-decoration:underline;margin-top:6px;display:block}
.promo2{left:436px;width:329px;background:#f0c232}
.promo2 .pic{left:0;top:0;width:150px;height:163px;background:linear-gradient(180deg,#d6a24a,#7b4d2a)}
.promo2 .title{left:160px;top:22px;font-size:28px;color:#c62828;font-weight:700}
.promo2 .price{left:245px;top:60px;width:54px;height:54px;border-radius:50%;background:#fff;color:var(--red);font-size:17px;display:flex;align-items:center;justify-content:center}
.promo2 .shop{left:240px;top:124px;font-size:11px;font-weight:700;text-decoration:underline;color:#222}
.promo3{left:779px;width:328px;background:#000;color:#fff}
.promo3 .frame{left:14px;top:14px;width:300px;height:135px;border:3px solid #fff}
.promo3 .save{left:30px;top:30px;font-size:38px;font-weight:700;line-height:36px}
.promo3 .pct{left:150px;top:22px;font-size:78px;font-weight:900;line-height:80px}
.promo3 .sel{left:34px;top:112px;font-size:25px;font-weight:300;background:#000;padding:0 4px}

/* featured */
.sectitle{left:0;width:1200px;text-align:center;font-size:42px;font-weight:400;color:#111}
.sectitle b{font-weight:700}
.arrow{width:20px;height:30px;display:flex;align-items:center;justify-content:center}
.card{top:993px;width:292px;height:305px;border:1px solid #bbb;background:#fff;text-align:center}
.card .new{position:absolute;left:13px;top:9px;width:44px;height:44px;border-radius:50%;background:var(--gold);color:#fff;font-size:12px;font-weight:700;display:flex;align-items:center;justify-content:center}
.card .swatch{position:absolute;right:16px;top:11px;display:flex;flex-direction:column;gap:7px}
.card .swatch i{width:8px;height:8px;border-radius:50%;display:block}
.card .pic{position:absolute;left:56px;top:50px;width:180px;height:155px;border-radius:6px}
.card .stars{position:absolute;top:226px;left:0;width:100%}
.card .nm{position:absolute;top:245px;left:0;width:100%;font-size:17px;color:#222}
.card .pr{position:absolute;top:269px;left:0;width:100%;font-size:18px;font-weight:700;color:var(--red)}
.stars{font-size:12px;letter-spacing:1px;color:var(--orange)}
.stars .off{color:#aaa}

/* special offer */
.special{top:1371px;left:0;width:1200px;height:386px;background:linear-gradient(120deg,#6b5a4d,#8f7d6d 45%,#5d4e43);color:#fff;text-align:center}
.special .kicker{position:absolute;top:80px;width:100%;letter-spacing:12px;font-size:20px;color:var(--gold)}
.special .band{position:absolute;left:214px;top:133px;width:772px;height:66px;background:rgba(196,140,20,.55)}
.special h2{position:absolute;top:100px;width:100%;font-size:88px;font-weight:700;letter-spacing:1px}
.special .extra{position:absolute;top:210px;width:100%;font-size:29px;font-weight:500;letter-spacing:4px}
.special .btn{position:absolute;left:526px;top:260px;width:148px;height:51px;background:var(--orange);font-size:20px;font-weight:500;display:flex;align-items:center;justify-content:center}

/* lists */
.panel{top:1831px;width:315px;height:566px;border:1px solid #aaa}
.panel .head{height:66px;border-bottom:1px solid #aaa;display:flex;align-items:center;padding:0 24px;font-size:23px;font-weight:500;color:#111}
.panel .head span{margin-left:auto;font-size:18px}
.item{position:absolute;left:28px;width:260px;height:62px}
.item .thumb{position:absolute;left:0;top:0;width:101px;height:62px;background:linear-gradient(135deg,#333,#9a7a48 60%,#2a2a2a)}
.item .stars{position:absolute;left:113px;top:-6px;font-size:11px}
.item .desc{position:absolute;left:113px;top:9px;font-size:12px;line-height:14px;color:#555;width:140px}
.item .pr{position:absolute;left:114px;top:41px;font-size:12px;font-weight:700;color:var(--red)}
.onsale{top:1870px;left:438px;width:326px;text-align:center}
.onsale .k{color:var(--orange);font-size:22px;font-weight:500}
.onsale .t{font-size:30px;font-weight:500;color:#111;margin-top:2px}
.onsale .pic{margin-top:10px;width:326px;height:352px;background:linear-gradient(180deg,#b9c9de,#6a92c8 50%,#c8d0d8)}
.onsale .stars{font-size:19px;margin-top:16px}
.onsale .nm{font-size:20px;color:#222;margin-top:2px}
.onsale .pr{font-size:19px;font-weight:700;color:var(--red);margin-top:4px}
.circ{width:30px;height:30px;border-radius:50%;background:#fff;border:1px solid #ccc;display:flex;align-items:center;justify-content:center}

/* features */
.features{top:2451px;left:0;width:1200px;height:174px;background:#f7f7f7}
.feat{position:absolute;top:59px;display:flex;align-items:center;gap:14px}
.feat .ic{width:58px;height:58px;border-radius:50%;border:1px solid #bbb;background:#fff;display:flex;align-items:center;justify-content:center}
.feat b{display:block;font-size:13px;font-weight:500;color:#111}
.feat span{font-size:13px;color:#444}

/* blog */
.post{top:2758px;width:324px}
.post .pic{height:254px}
.post .date{margin-top:10px;font-size:13px;color:var(--orange)}
.post h3{font-size:19px;font-weight:500;line-height:22px;color:#222;margin-top:3px}
.post p{font-size:12.5px;line-height:18px;color:#666;margin-top:6px}

/* footer */
.footer{top:3220px;left:0;width:1200px;height:338px;background:var(--dark);color:#ddd}
.footer .fbrand{left:94px;top:38px;display:flex;flex-direction:column;align-items:flex-start}
.footer .fbrand .mark{width:40px;height:40px;background:#fff;margin-left:16px}
.footer .fbrand .name{font-size:21px;font-weight:700;color:#fff;margin-top:2px}
.footer .about{left:94px;top:118px;width:290px;font-size:13px;line-height:20px}
.footer .social{left:94px;top:196px;display:flex;gap:9px}
.footer .social i{width:28px;height:28px;border-radius:50%;border:2px solid #fff;display:block}
.fcol{position:absolute;top:64px;font-size:13px}
.fcol h4{font-size:14px;font-weight:500;color:#fff;margin-bottom:14px}
.fcol li{list-style:none;margin-bottom:12px}
.pay{right:92px;top:228px;text-align:right}
.pay .coin{font-size:22px;font-weight:700;color:#fff}
.pay .cards{display:flex;gap:4px;margin-top:8px}
.pay .cards i{width:36px;height:22px;border-radius:2px;background:#fff;display:block}
.copyright{top:3558px;left:0;width:1200px;height:44px;background:#000;color:#ddd;font-size:13px;text-align:center;line-height:44px}
</style>
</head>
<body>

<div class="abs topbar">
  <span class="abs welcome">Default welcome message!</span>
  <span class="abs lang">English ⌄</span>
</div>

<header class="abs header">
  <div class="abs brand"><span class="mark"></span><span class="name">Morvena</span></div>
  <div class="abs search">
    <div class="cat">All Categories ▾</div>
    <div class="field">Sarch Product...</div>
    <div class="btn"><svg width="14" height="14" viewBox="0 0 14 14"><circle cx="6" cy="6" r="4.5" stroke="#fff" stroke-width="1.8" fill="none"/><line x1="9.3" y1="9.3" x2="13" y2="13" stroke="#fff" stroke-width="1.8"/></svg></div>
  </div>
  <div class="abs hicons">
    <span><span class="ico"><svg width="16" height="14" viewBox="0 0 16 14"><path d="M8 13 1.5 6.5A3.5 3.5 0 0 1 8 2a3.5 3.5 0 0 1 6.5 4.5Z" fill="#fff"/></svg></span>Wishlist(0)</span>
    <span><span class="ico"><svg width="18" height="16" viewBox="0 0 18 16"><path d="M1 2h3l2 8h9l2-6H5" stroke="#fff" stroke-width="1.6" fill="none"/><circle cx="7" cy="13.5" r="1.4" fill="#fff"/><circle cx="14" cy="13.5" r="1.4" fill="#fff"/></svg></span>0.00</span>
  </div>
</header>

<nav class="abs nav">
  <div class="abs cats">
    <svg width="14" height="11" viewBox="0 0 14 11"><path d="M0 1h14M0 5.5h14M0 10h14" stroke="#fff" stroke-width="1.6"/></svg>
    CATEGORIES
    <span class="chev"><svg width="10" height="6" viewBox="0 0 10 6"><path d="M1 1l4 4 4-4" stroke="#3a3a3a" stroke-width="1.8" fill="none"/></svg></span>
  </div>
  <ul class="abs">
    <li>New Arrivals</li><li>Preorder</li><li>Women'sCollection</li><li>Men's Collection</li><li>Summer 2020 Collection</li><li>Winter 2020Collection</li><li>BagsAccessories</li>
  </ul>
</nav>

<section class="abs hero">
  <div class="abs model" role="img" aria-label="Woman in hat and grey outfit holding a black leather handbag"></div>
  <div class="abs boots" role="img" aria-label="Pair of black leather lace-up boots with red soles"></div>
  <div class="abs hero-copy">
    <div class="kicker">FREE SHOPPING</div>
    <h1>WOMEN SHOES<br>AND BAGS</h1>
    <div class="tag">MINIMUM 30%OFF</div>
  </div>
  <div class="abs dots"><i></i><i></i><i></i></div>
</section>

<div class="abs promo promo1">
  <div class="abs pic" role="img" aria-label="Lilac lace-up sneakers"></div>
  <div class="abs txt">WOMEN SHOES<div class="off">-80% OFF</div><span class="shop">SHOP NOW</span></div>
</div>
<div class="abs promo promo2">
  <div class="abs pic" role="img" aria-label="Woman with sunglasses holding a brown handbag"></div>
  <div class="abs title">Hand Bag</div>
  <div class="abs price">R49</div>
  <div class="abs shop">SHOP NOW</div>
</div>
<div class="abs promo promo3">
  <div class="abs frame"></div>
  <div class="abs save">SAVE<br>UPTO</div>
  <div class="abs pct">50%</div>
  <div class="abs sel">ON SELECTED ITEMS</div>
</div>

<h2 class="abs sectitle" style="top:908px">FEATURED <b>PRODUCTS</b></h2>
<div class="abs arrow" style="left:107px;top:1131px"><svg width="12" height="22" viewBox="0 0 12 22"><path d="M10 2 2 11l8 9" stroke="#222" stroke-width="2" fill="none"/></svg></div>
<div class="abs arrow" style="left:1073px;top:1131px"><svg width="12" height="22" viewBox="0 0 12 22"><path d="M2 2l8 9-8 9" stroke="#222" stroke-width="2" fill="none"/></svg></div>

<div class="abs card" style="left:138px">
  <span class="new">NEW</span>
  <span class="swatch"><i style="background:#1a7fd6"></i><i style="background:#e2361a"></i><i style="background:#111"></i></span>
  <div class="pic" role="img" aria-label="Red patent stiletto pump" style="background:linear-gradient(135deg,#fff 30%,#e33 55%,#fff 80%)"></div>
  <div class="stars">★★★<span class="off">★★</span></div>
  <div class="nm">Contrary to popular</div>
  <div class="pr">R100.72</div>
</div>
<div class="abs card" style="left:453px">
  <span class="swatch"><i style="background:#17a89a"></i><i style="background:#e2361a"></i><i style="background:#f08a1a"></i></span>
  <div class="pic" role="img" aria-label="Pink suede block heel pump" style="background:linear-gradient(135deg,#fff 25%,#d9676e 55%,#f2f2f2 85%)"></div>
  <div class="stars">★★★★<span class="off">★</span></div>
  <div class="nm">Contrary to popular</div>
  <div class="pr">R105.72</div>
</div>
<div class="abs card" style="left:768px">
  <span class="new">NEW</span>
  <span class="swatch"><i style="background:#1a7fd6"></i><i style="background:#e2361a"></i><i style="background:#111"></i></span>
  <div class="pic" role="img" aria-label="Peach leather tote handbag" style="background:linear-gradient(180deg,#fff 10%,#f2b8a2 50%,#eee 95%)"></div>
  <div class="stars">★★★<span class="off">★★</span></div>
  <div class="nm">Contrary to popular</div>
  <div class="pr">R100.72</div>
</div>

<section class="abs special" role="img" aria-label="Red heels on a mosaic tiled floor">
  <div class="kicker">SPECIAL OFFER FOR YOU</div>
  <div class="band"></div>
  <h2>WOMEN SHOES</h2>
  <div class="extra">EXTRA 50% OFF</div>
  <div class="btn">Shop Now</div>
</section>

<div class="abs panel" style="left:94px">
  <div class="head">TOP PRODUCTS<span>‹ ›</span></div>
  <div class="item" style="top:94px"><div class="thumb" role="img" aria-label="Gold stiletto heels"></div><div class="stars">★★★<span class="off">★★</span></div><div class="desc">It is a long established fact that</div><div class="pr">R105</div></div>
  <div class="item" style="top:185px"><div class="thumb" role="img" aria-label="Gold stiletto heels"></div><div class="stars">★★★<span class="off">★★</span></div><div class="desc">It is a long established fact that</div><div class="pr">R105</div></div>
  <div class="item" style="top:277px"><div class="thumb" role="img" aria-label="Gold stiletto heels"></div><div class="stars">★★★<span class="off">★★</span></div><div class="desc">It is a long established fact that</div><div class="pr">R105</div></div>
  <div class="item" style="top:368px"><div class="thumb" role="img" aria-label="Gold stiletto heels"></div><div class="stars">★★★<span class="off">★★</span></div><div class="desc">It is a long established fact that</div><div class="pr">R105</div></div>
  <div class="item" style="top:456px"><div class="thumb" role="img" aria-label="Gold stiletto heels"></div><div class="stars">★★★<span class="off">★★</span></div><div class="desc">It is a long established fact that</div><div class="pr">R105</div></div>
</div>

<div class="abs onsale">
  <div class="k">ON SALE</div>
  <div class="t">MEN’S COLLECTION</div>
  <div class="pic" role="img" aria-label="Man in blue denim shirt and jeans"></div>
  <div class="stars">★★★★<span class="off">★</span></div>
  <div class="nm">Contrary to popular</div>
  <div class="pr">R105.72</div>
</div>
<div class="abs circ" style="left:422px;top:2101px"><svg width="8" height="12" viewBox="0 0 8 12"><path d="M6 1 1 6l5 5" stroke="#333" stroke-width="1.6" fill="none"/></svg></div>
<div class="abs circ" style="left:750px;top:2101px"><svg width="8" height="12" viewBox="0 0 8 12"><path d="M2 1l5 5-5 5" stroke="#333" stroke-width="1.6" fill="none"/></svg></div>

<div class="abs panel" style="left:793px;top:1829px">
  <div class="head">BEST SELLER<span>‹ ›</span></div>
  <div class="item" style="top:94px"><div class="thumb" role="img" aria-label="Gold stiletto heels"></div><div class="stars">★★★<span class="off">★★</span></div><div class="desc">It is a long established fact that</div><div class="pr">R105</div></div>
  <div class="item" style="top:185px"><div class="thumb" role="img" aria-label="Gold stiletto heels"></div><div class="stars">★★★<span class="off">★★</span></div><div class="desc">It is a long established fact that</div><div class="pr">R105</div></div>
  <div class="item" style="top:277px"><div class="thumb" role="img" aria-label="Gold stiletto heels"></div><div class="stars">★★★<span class="off">★★</span></div><div class="desc">It is a long established fact that</div><div class="pr">R105</div></div>
  <div class="item" style="top:368px"><div class="thumb" role="img" aria-label="Gold stiletto heels"></div><div class="stars">★★★<span class="off">★★</span></div><div class="desc">It is a long established fact that</div><div class="pr">R105</div></div>
  <div class="item" style="top:456px"><div class="thumb" role="img" aria-label="Gold stiletto heels"></div><div class="stars">★★★<span class="off">★★</span></div><div class="desc">It is a long established fact that</div><div class="pr">R105</div></div>
</div>

<section class="abs features">
  <div class="feat" style="left:102px"><span class="ic"><svg width="26" height="26" viewBox="0 0 26 26"><path d="M5 21 9 13l8-8 4 0 0 4-8 8Z" stroke="#222" stroke-width="1.8" fill="none"/><path d="M3 23l4-4" stroke="#222" stroke-width="1.8"/></svg></span><div><b>Free Shipping Worldwide</b><span>All Orders</span></div></div>
  <div class="feat" style="left:358px"><span class="ic"><svg width="26" height="26" viewBox="0 0 26 26"><circle cx="13" cy="10" r="5" fill="#222"/><path d="M5 24a8 8 0 0 1 16 0Z" fill="#222"/><path d="M6 11a7 7 0 0 1 14 0" stroke="#222" stroke-width="1.6" fill="none"/></svg></span><div><b>Online 24/7 Supports</b><span>Sign Up For Gift</span></div></div>
  <div class="feat" style="left:614px"><span class="ic"><svg width="28" height="22" viewBox="0 0 28 22"><rect x="3" y="5" width="22" height="12" rx="2" stroke="#222" stroke-width="1.8" fill="none"/><circle cx="14" cy="11" r="3" fill="#222"/></svg></span><div><b>14-Days Money Back</b><span>Sign Up For Gift</span></div></div>
  <div class="feat" style="left:870px"><span class="ic"><svg width="26" height="26" viewBox="0 0 26 26"><rect x="8" y="3" width="10" height="9" fill="#222"/><path d="M3 18h8l4 3 8-4v5H3Z" fill="#222"/></svg></span><div><b>Win $100 First Purchase</b><span>Sign Up For Voucher</span></div></div>
</section>

<h2 class="abs sectitle" style="top:2675px">LATEST <b>BLOG</b></h2>

<article class="abs post" style="left:94px">
  <div class="pic" role="img" aria-label="Woman in orange coat sitting in a shoe boutique" style="background:linear-gradient(135deg,#e9e5e1,#c4683a 50%,#eee)"></div>
  <div class="date">Date 7 Dec 2020</div>
  <h3>Lorem Ipsum is simply<br>dummy text</h3>
  <p>It is a long established fact that a reader will be distracted by the readable content of a page when looking at its layout.</p>
</article>
<article class="abs post" style="left:438px">
  <div class="pic" role="img" aria-label="Couple sitting with leather bags on a wooden pallet" style="background:linear-gradient(135deg,#4a4a4a,#7a6a5e 55%,#2e2e2e)"></div>
  <div class="date">Date 7 Dec 2020</div>
  <h3>Lorem Ipsum is simply<br>dummy text</h3>
  <p>It is a long established fact that a reader will be distracted by the readable content of a page when looking at its layout.</p>
</article>
<article class="abs post" style="left:782px">
  <div class="pic" role="img" aria-label="Legs in red high heels against a dark brick wall" style="background:linear-gradient(135deg,#2a2a2a,#4b4b4b 50%,#c41e1e 90%)"></div>
  <div class="date">Date 7 Dec 2020</div>
  <h3>Lorem Ipsum is simply<br>dummy text</h3>
  <p>It is a long established fact that a reader will be distracted by the readable content of a page when looking at its layout.</p>
</article>

<footer class="abs footer">
  <div class="abs fbrand"><span class="mark"></span><span class="name">Morvena</span></div>
  <p class="abs about">It is a long established fact that a reader will be distracted by the readable content of a page when looking at its layout.</p>
  <div class="abs social"><i aria-label="Social profile"></i><i aria-label="Social profile"></i></div>
  <div class="fcol" style="left:416px"><h4>Festival Deals</h4><ul><li>Home</li><li>Comparison Product</li><li>Shop</li><li>Reviews</li><li>Blog</li></ul></div>
  <div class="fcol" style="left:609px"><h4>Need Help ?</h4><ul><li>Getting Started</li><li>Contact Us</li><li>FAQ's</li><li>Press</li><li>Product Feed</li><li>Best Rated Product</li><li>Feature product</li></ul></div>
  <div class="fcol" style="left:788px"><h4>About</h4><ul><li>Privacy</li><li>Return Policy</li><li>Order &amp; Return</li><li>Terms &amp; Conditions</li></ul></div>
  <div class="fcol" style="left:976px;width:140px"><h4>Contact Us</h4><ul><li style="line-height:19px">It is a long established fact that a reader</li><li>45870231</li><li>info@morvena.com</li></ul></div>
  <div class="abs pay">
    <div class="coin">CoinLane</div>
    <div class="cards"><i></i><i></i><i></i><i></i></div>
  </div>
</footer>
<div class="abs copyright">© 2020Morvena. All Right Reserved.</div>

</body>
</html>
```